Attorney At Law Card Design

I am an attorney. I need something simple but elegant with nice conservative colors. The design should communicate competence, and confidence. I specialize in Personal Injury and Criminal Defense Work.

Industry/Entity Type

Conservative

Contact Information for Business Card

Delvaqui Law Firm
2837 Harlow Ave.
McAllen, TX 76213

Matías "Matt" Delvaqui
512-437-2619 Tel.
512-437-2614 Fax
512-782-5063 Cell

Justice for All

```html
<!DOCTYPE html>
<html lang="en">
<head>
<meta charset="utf-8">
<title>Delvaqui Law Firm – Business Card</title>
<link href="https://fonts.googleapis.com/css2?family=PT+Sans:wght@400;700&display=swap" rel="stylesheet">
<style>
  :root {
    --frame: #333f3f;
    --paper: #ffffff;
    --teal: #3cc4d4;
    --ink: #333f3f;
    --muted: #5a6464;
    --box-edge: #eeeeee;
  }
  html, body {
    margin: 0;
    padding: 0;
    width: 1200px;
    height: 653px;
    overflow: hidden;
    background: var(--paper);
  }
  .card {
    position: relative;
    width: 1200px;
    height: 653px;
    box-sizing: border-box;
    border: 17px solid var(--frame);
    background: var(--paper);
    font-family: "PT Sans", "Tahoma", sans-serif;
    overflow: hidden;
  }
  .rule {
    position: absolute;
    top: 273px;
    height: 2px;
    background: var(--teal);
  }
  .rule--left { left: 0; width: 579px; }
  .rule--right { left: 830px; width: 336px; }

  .firm-name {
    position: absolute;
    left: 56px;
    top: 225px;
    margin: 0;
    font-size: 37px;
    font-weight: 400;
    line-height: 1;
    letter-spacing: 0.01em;
    color: var(--teal);
    text-transform: uppercase;
  }
  .street {
    position: absolute;
    left: 56px;
    top: 289px;
    margin: 0;
    font-size: 28px;
    line-height: 1;
    color: var(--muted);
  }

  .mark-box {
    position: absolute;
    left: 589px;
    top: 170px;
    width: 240px;
    height: 194px;
    box-sizing: border-box;
    border: 1px solid var(--box-edge);
    background: var(--paper);
    display: flex;
    align-items: center;
    justify-content: center;
    gap: 10px;
  }
  .mark-box__square {
    width: 14px;
    height: 14px;
    background: var(--ink);
  }
  .mark-box__name {
    font-size: 30px;
    font-weight: 700;
    color: var(--ink);
    line-height: 1;
  }
  .tagline {
    position: absolute;
    left: 589px;
    width: 240px;
    top: 373px;
    margin: 0;
    text-align: center;
    font-size: 13px;
    letter-spacing: 0.55em;
    padding-left: 0.55em;
    box-sizing: border-box;
    color: var(--muted);
    text-transform: uppercase;
  }

  .contact {
    position: absolute;
    right: 42px;
    margin: 0;
    text-align: right;
    font-size: 20px;
    line-height: 1;
    color: var(--ink);
  }
  .contact--city { top: 219px; }
  .contact--person { top: 243px; }
  .contact-list {
    position: absolute;
    right: 42px;
    top: 294px;
    margin: 0;
    padding: 0;
    list-style: none;
    font-size: 20px;
    color: var(--ink);
  }
  .contact-list li {
    line-height: 31px;
    text-align: left;
  }
  .contact-list .label {
    display: inline-block;
    width: 51px;
  }
</style>
</head>
<body>
  <main class="card">
    <div class="rule rule--left"></div>
    <div class="rule rule--right"></div>

    <h1 class="firm-name">Delvaqui Law Firm</h1>
    <p class="street">2837 Harlow Ave. McAllen</p>

    <div class="mark-box">
      <span class="mark-box__square"></span>
      <span class="mark-box__name">Delvaqui</span>
    </div>
    <p class="tagline">Justice for All</p>

    <p class="contact contact--city">McAllen, TX 76213</p>
    <p class="contact contact--person">Matías "Matt" Delvaqui</p>
    <ul class="contact-list">
      <li><span class="label">Tel.</span>512-437-2619</li>
      <li><span class="label">Fax</span>512-437-2614</li>
      <li><span class="label">Cell</span>512-782-5063</li>
    </ul>
  </main>
</body>
</html>
```